LAW FIRM - RE-DESIGN - (professional, excellence, tradition and innovation)

We are a premier law firm in New South Wales, Australia. We pride ourselves on being cutting edge and up to date in our market.

Our firm formed in 1874 and has a particularly strong tradition within it's geographic footprint. acting for clients over multiple generations. Despite our regional background, our reputation for excellence has enable us to remain highly visible in a large area.

We have invested heavily in ensuring future planning of this business, and do so on a recurring basis. This has lead to a review of our existing web site.

Although serviceable we feel our previous website is out-of-date and not as in touch with the modern market. We are aware that for the emerging clients a web site is often the face of a firm and a failure to hold attention on the first page may fail to capture the client.

We are seeking designs to communicate the core values of professionalism and excellence. At the same time as maintaining traditional country values of honesty, integrity and hard work we strive to embrace changes to the law and technology.

Target Market(s)

Clients of Law Firm

Industry/Entity Type

Law Firm

Coding

Coded - Design and coding required

Number of Pages Required

5+ page

Requirements
Must have
• A strong sense of professionalism and excellence with a careful balance between traditional values and innovation.
Nice to have
• We have included within our design brief links to top competitors sites to assist for design concepts.

```html
<!DOCTYPE html>
<html lang="en">
<head>
<meta charset="utf-8">
<title>RTM Law</title>
<link href="https://fonts.googleapis.com/css2?family=Cinzel:wght@400;700&family=Arimo:wght@400;700&display=swap" rel="stylesheet">
<style>
:root{
  --navy:#0f3a6e;
  --navy-deep:#0b2f5c;
  --bar:#163b6c;
  --ink:#333;
  --muted:#555;
  --light:#ececec;
  --line:#c9cfd8;
  --white:#fff;
}
*{box-sizing:border-box;margin:0;padding:0}
html,body{width:1200px;height:3371px;overflow:hidden}
body{font-family:"Arimo",Arial,sans-serif;color:var(--ink);background:var(--white);position:relative}
.serif{font-family:"Cinzel",Georgia,serif}
.btn{display:inline-flex;align-items:center;justify-content:center;background:var(--navy);color:var(--white);font-family:"Cinzel",Georgia,serif;font-weight:700;font-size:21px;letter-spacing:1px;border-radius:4px;position:absolute}
.abs{position:absolute}

/* top bar */
.topbar{position:absolute;left:0;top:0;width:1200px;height:40px;background:var(--bar);color:var(--white);font-size:16px}
.topbar .item{position:absolute;top:10px;display:flex;align-items:center;gap:8px}

/* header */
.header{position:absolute;left:0;top:40px;width:1200px;height:113px;background:var(--white)}
.brand{position:absolute;left:79px;top:22px;display:flex;align-items:center;gap:12px;font-family:"Cinzel",Georgia,serif;font-weight:700;font-size:40px;color:var(--navy)}
.brand .mark{width:22px;height:22px;border-radius:50%;background:var(--navy)}
.nav{position:absolute;right:79px;top:34px;display:flex;gap:6px;font-size:16px}
.nav a{color:#222;text-decoration:none;padding:14px 14px;border-radius:3px}
.nav a.active{background:var(--navy);color:var(--white);padding:14px 22px}

/* hero */
.hero{position:absolute;left:0;top:153px;width:1200px;height:526px;background:linear-gradient(90deg,#e9ecef 0%,#dfe3e7 40%,#9aa3ad 62%,#6d7782 100%)}
.hero-title{position:absolute;left:79px;top:140px;font-family:"Cinzel",Georgia,serif;font-size:82px;color:#111;letter-spacing:2px}
.hero-text{position:absolute;left:79px;top:238px;width:600px;font-size:20px;line-height:30px;color:#222}
.dots{position:absolute;left:545px;top:480px;display:flex;gap:14px}
.dots span{width:14px;height:14px;border-radius:50%;border:2px solid #fff;background:rgba(255,255,255,.4)}
.dots span.on{background:#fff}

/* welcome */
.section-title{font-family:"Cinzel",Georgia,serif;color:var(--navy);text-align:center;font-size:50px;font-weight:700;letter-spacing:1px}
.welcome{position:absolute;left:0;top:679px;width:1200px;height:388px}
.welcome .section-title{position:absolute;left:0;width:1200px;top:50px}
.welcome p{position:absolute;left:155px;width:890px;text-align:center;font-size:14px;line-height:24px;color:var(--muted)}

/* banded titles */
.band{position:absolute;left:0;width:1200px;background:linear-gradient(180deg,#1f4c86 0%,#123e74 60%,#0d3468 100%)}
.band .section-title{color:var(--white);font-weight:400;position:absolute;left:0;width:1200px}

/* services */
.card{position:absolute;top:1281px;width:333px;height:393px;background:var(--navy);color:var(--white);text-align:center}
.card .photo{height:206px;background:linear-gradient(160deg,#8fa0b5,#45566d)}
.card h3{font-family:"Cinzel",Georgia,serif;font-size:19px;font-weight:700;margin-top:30px;letter-spacing:.5px}
.card p{font-size:14px;line-height:24px;margin:10px 22px 0}
.card svg{margin-top:6px}

/* partners */
.partner{position:absolute;top:1950px;width:184px;height:261px}
.partner .frame{height:180px;background:#e6e6e6;padding:18px 22px 0}
.partner .photo{height:162px;background:linear-gradient(180deg,#6d5a45,#3a3a44)}
.partner .name{height:45px;background:var(--white);font-family:"Cinzel",Georgia,serif;font-weight:700;font-size:17px;color:#111;display:flex;align-items:center;justify-content:center;letter-spacing:.5px}
.partner .since{height:36px;background:#000;color:var(--white);font-size:15px;display:flex;align-items:center;justify-content:center}

/* about + contact */
.h2{font-family:"Cinzel",Georgia,serif;font-weight:700;font-size:42px;color:var(--navy)}
.about p{font-size:14px;line-height:24px;color:var(--muted)}
.field{position:absolute;left:664px;width:448px;border:1px solid var(--line);background:var(--white);font-size:14px;color:#888;padding:12px 14px}
.field svg{position:absolute;right:12px;top:50%;transform:translateY(-50%)}

/* philosophy */
.philosophy{position:absolute;left:0;top:2824px;width:1200px;height:239px;background:var(--light)}

/* footer */
.footer{position:absolute;left:0;top:3063px;width:1200px;height:308px;background:var(--navy-deep);color:var(--white)}
.footer h4{font-family:"Cinzel",Georgia,serif;font-weight:700;font-size:17px;letter-spacing:.5px;position:absolute;top:47px}
.office{position:absolute;top:90px;font-size:14px;line-height:21px;color:#d5dce6}
.office .row{display:flex;gap:12px;align-items:flex-start;margin-bottom:12px}
.office .row svg{flex:none}
</style>
</head>
<body>

<div class="topbar">
  <div class="item" style="left:755px">
    <svg width="16" height="16" viewBox="0 0 24 24"><path fill="#fff" d="M6.6 10.8a15 15 0 0 0 6.6 6.6l2.2-2.2c.3-.3.7-.4 1-.2 1.1.4 2.3.6 3.6.6.6 0 1 .4 1 1V20c0 .6-.4 1-1 1A17 17 0 0 1 3 4c0-.6.4-1 1-1h3.5c.6 0 1 .4 1 1 0 1.3.2 2.5.6 3.6.1.3 0 .7-.2 1z"/></svg>026700 1200
  </div>
  <div class="item" style="left:905px">
    <svg width="18" height="14" viewBox="0 0 18 14"><rect x="1" y="1" width="16" height="12" fill="#fff"/><path d="M1 1l8 6 8-6" stroke="#163b6c" stroke-width="1.5" fill="none"/></svg>reception@rtmlaw.com.au
  </div>
</div>

<header class="header">
  <div class="brand"><span class="mark"></span>RTM Law</div>
  <nav class="nav">
    <a class="active">HOME</a><a>ABOUT US</a><a>SERVICES</a><a>OUR PEOPLE</a><a>FAQ'S</a><a>CONTACT US</a>
  </nav>
</header>

<section class="hero" role="img" aria-label="Photo of lawyers meeting with a client around a desk in a bright office">
  <h1 class="hero-title">RTM LAW</h1>
  <p class="hero-text">RTM law is a legal firm geographically based within the New England region of New South Wales, Australia.</p>
  <span class="btn" style="left:79px;top:314px;width:186px;height:54px">CONTACT US</span>
  <div class="dots"><span class="on"></span><span></span><span></span><span></span></div>
</section>

<section class="welcome">
  <h2 class="section-title">WELCOME TO RTM LAW</h2>
  <p style="top:120px">RTM Law has been in existence since 1874 originally starting out as the firm Walter Greaves of Glen Innes. In 1894 Walter Greaves was acquired by Colonel HL Marsh. The firm became known as RL Marsh &amp; Co. until early 1970 when it became Marsh &amp; Co, Marsh Tennant &amp; Co in 1979 and Marsh Tennant &amp; Rowe in 1982.</p>
  <p style="top:208px">In December 1999, the firm opened an office in Inverell taking over the practice of JD Hollis &amp; Associates. This was followed by the incorporation of Pemberton &amp; Co in December 2000 and the Armidale office moved to larger premises in Linden Street.</p>
  <span class="btn" style="left:512px;top:271px;width:176px;height:54px">KNOW MORE</span>
</section>

<section class="band" style="top:1067px;height:169px" role="img" aria-label="Blue-tinted photo of a busy city crowd">
  <h2 class="section-title" style="top:58px">OUR SERVICES</h2>
</section>

<article class="card" style="left:79px">
  <div class="photo" role="img" aria-label="Photo of a glass and steel building roof"></div>
  <h3>BUILDING &amp; CONSTRUCTION</h3>
  <p>Our team can help draft and advise on building contracts for a home, commercial or industrial buildings, as well as represent</p>
  <svg width="20" height="20" viewBox="0 0 20 20"><path d="M4 4l6 5 6-5M4 10l6 5 6-5" stroke="#fff" stroke-width="2" fill="none"/></svg>
</article>
<article class="card" style="left:434px">
  <div class="photo" role="img" aria-label="Photo of a business handshake in front of office towers" style="background:linear-gradient(160deg,#9fb3cc,#3f5a80)"></div>
  <h3>CORPORATE &amp; COMMERCIAL</h3>
  <p>Our team can help draft and advise on building contracts for a home, commercial or industrial buildings, as well as represent</p>
  <svg width="20" height="20" viewBox="0 0 20 20"><path d="M4 4l6 5 6-5M4 10l6 5 6-5" stroke="#fff" stroke-width="2" fill="none"/></svg>
</article>
<article class="card" style="left:789px">
  <div class="photo" role="img" aria-label="Photo of handcuffed hands" style="background:linear-gradient(160deg,#5a4a40,#1f1f22)"></div>
  <h3>CRIMINAL LAW</h3>
  <p>Our team can help draft and advise on building contracts for a home, commercial or industrial buildings, as well as represent</p>
  <svg width="20" height="20" viewBox="0 0 20 20"><path d="M4 4l6 5 6-5M4 10l6 5 6-5" stroke="#fff" stroke-width="2" fill="none"/></svg>
</article>
<span class="btn" style="left:526px;top:1696px;width:146px;height:54px">VIEW ALL</span>

<section class="band" style="top:1813px;height:468px;background:linear-gradient(135deg,#2a5a94 0%,#164680 50%,#0f3a6e 100%)" role="img" aria-label="Blue-tinted photo of a modern office interior">
  <h2 class="section-title" style="top:55px">OUR PARTNERS</h2>
  <svg class="abs" style="left:26px;top:240px" width="18" height="40" viewBox="0 0 18 40"><path d="M16 2L3 20l13 18" stroke="#fff" stroke-width="2" fill="none"/></svg>
  <svg class="abs" style="left:1156px;top:240px" width="18" height="40" viewBox="0 0 18 40"><path d="M2 2l13 18L2 38" stroke="#fff" stroke-width="2" fill="none"/></svg>
</section>

<div class="partner" style="left:79px"><div class="frame"><div class="photo" role="img" aria-label="Portrait of partner Colin Tennant"></div></div><div class="name">COLIN TENNANT</div><div class="since">Admitted as a1977</div></div>
<div class="partner" style="left:290px"><div class="frame"><div class="photo" role="img" aria-label="Portrait of partner Hugh Rowe"></div></div><div class="name">HUGH ROWE</div><div class="since">Admitted as a1977</div></div>
<div class="partner" style="left:505px"><div class="frame"><div class="photo" role="img" aria-label="Portrait of partner Leah Tennant"></div></div><div class="name">LEAH TENNANT</div><div class="since">Admitted as a 2006</div></div>
<div class="partner" style="left:721px"><div class="frame"><div class="photo" role="img" aria-label="Portrait of partner Daniel Wu Lin"></div></div><div class="name">DANIEL WU LIN</div><div class="since">Admitted as a 2006</div></div>
<div class="partner" style="left:935px"><div class="frame"><div class="photo" role="img" aria-label="Portrait of partner Nina Foster"></div></div><div class="name">NINA FOSTER</div><div class="since">Admitted as a 2002</div></div>

<section class="about">
  <h2 class="h2 abs" style="left:79px;top:2333px">ABOUT US</h2>
  <div class="abs" style="left:79px;top:2395px;font-size:20px;color:#333">RTM LAW</div>
  <p class="abs" style="left:79px;top:2432px;width:510px">RTM Law has been in existence since 1874 originally starting out as the firm Walter Greaves of Glen Innes. In 1894 Walter Greaves was acquired by Colonel HL Marsh. The firm became known as RL Marsh &amp; Co. until early 1970 when it became Marsh &amp; Co, Marsh Tennant &amp; Co in 1979 and Marsh Tennant &amp; Rowe in 1982.</p>
  <p class="abs" style="left:79px;top:2564px;width:510px">In December 1999, the firm opened an office in Inverell taking over the practice of JD Hollis &amp; Associates. This was followed by the incorporation of Pemberton &amp; Co in December 2000 and the Armidale office moved to larger premises in Linden Street.</p>
  <span class="btn" style="left:79px;top:2694px;width:175px;height:54px">KNOW MORE</span>
  <div class="abs" style="left:600px;top:2300px;width:10px;height:470px;background:linear-gradient(90deg,rgba(0,0,0,.08),rgba(0,0,0,0))"></div>
</section>

<section class="contact">
  <h2 class="h2 abs" style="left:652px;width:460px;text-align:center;top:2333px">CONTACT US</h2>
  <p class="abs" style="left:652px;width:460px;text-align:center;top:2392px;font-size:14px;line-height:24px;color:var(--muted)">If you have a legal query leave your name, contact details and query, and one of our friendly staff will get in contact with you.</p>
  <div class="field" style="top:2458px;height:45px">Name*<svg width="14" height="14" viewBox="0 0 14 14"><circle cx="7" cy="4" r="3.2" fill="#777"/><path d="M1 14c0-4 3-6 6-6s6 2 6 6z" fill="#777"/></svg></div>
  <div class="field" style="top:2514px;height:41px">Email*<svg width="14" height="11" viewBox="0 0 14 11"><rect width="14" height="11" fill="#777"/><path d="M0 0l7 5 7-5" stroke="#fff" fill="none"/></svg></div>
  <div class="field" style="top:2566px;height:41px;width:221px">phone*<svg width="13" height="13" viewBox="0 0 24 24"><path fill="#777" d="M6.6 10.8a15 15 0 0 0 6.6 6.6l2.2-2.2c.3-.3.7-.4 1-.2 1.1.4 2.3.6 3.6.6.6 0 1 .4 1 1V20c0 .6-.4 1-1 1A17 17 0 0 1 3 4c0-.6.4-1 1-1h3.5c.6 0 1 .4 1 1 0 1.3.2 2.5.6 3.6.1.3 0 .7-.2 1z"/></svg></div>
  <div class="field" style="top:2566px;height:41px;left:892px;width:220px">phone*<svg width="14" height="8" viewBox="0 0 14 8"><path d="M0 0h14L7 8z" fill="#777"/></svg></div>
  <div class="field" style="top:2618px;height:76px">Message*</div>
  <span class="btn" style="left:816px;top:2703px;width:152px;height:56px">SUBMIT</span>
</section>

<section class="philosophy">
  <h2 class="h2 abs" style="left:77px;top:40px;font-weight:400;font-size:46px">OUR PHILOSOPHY</h2>
  <p class="abs" style="left:79px;top:105px;width:780px;font-size:14px;line-height:24px;color:var(--muted)">Driven by quality legal work and service, RTM Law is founded on and values integrity, honesty, personal excellence, mutual respect and commitment to team work.</p>
  <p class="abs" style="left:79px;top:157px;font-size:14px;color:var(--muted)">RTM Law is built on strength, independence, integrity and an enthusiasm for the law.</p>
  <svg class="abs" style="left:919px;top:26px" width="190" height="190" viewBox="0 0 190 190" role="img" aria-label="Specialist accreditation badge"><circle cx="95" cy="95" r="90" fill="none" stroke="#111" stroke-width="3"/><circle cx="95" cy="95" r="52" fill="#111"/></svg>
</section>

<footer class="footer">
  <div class="abs" style="left:101px;top:95px;display:flex;align-items:center;gap:12px;font-family:'Cinzel',Georgia,serif;font-weight:700;font-size:40px;color:#fff"><span style="width:22px;height:22px;border-radius:50%;background:#fff"></span>RTM Law</div>

  <h4 style="left:337px">ARMIDALE OFFICE</h4>
  <div class="office" style="left:337px;width:240px">
    <div class="row"><svg width="16" height="22" viewBox="0 0 16 22"><path d="M8 1a7 7 0 0 0-7 7c0 5 7 13 7 13s7-8 7-13a7 7 0 0 0-7-7z" fill="none" stroke="#fff" stroke-width="1.6"/><circle cx="8" cy="8" r="2.5" fill="none" stroke="#fff" stroke-width="1.6"/></svg><span>Suite 9 Carrow Arcade 40<br>-42 Elm StreetArmidale</span></div>
    <div class="row"><svg width="18" height="18" viewBox="0 0 24 24"><path fill="none" stroke="#fff" stroke-width="1.8" d="M6.6 10.8a15 15 0 0 0 6.6 6.6l2.2-2.2c.3-.3.7-.4 1-.2 1.1.4 2.3.6 3.6.6.6 0 1 .4 1 1V20c0 .6-.4 1-1 1A17 17 0 0 1 3 4c0-.6.4-1 1-1h3.5c.6 0 1 .4 1 1 0 1.3.2 2.5.6 3.6.1.3 0 .7-.2 1z"/></svg><span>026700 1200</span></div>
    <div class="row"><svg width="18" height="18" viewBox="0 0 18 18"><rect x="4" y="1" width="10" height="5" fill="none" stroke="#fff" stroke-width="1.5"/><rect x="1" y="6" width="16" height="7" fill="none" stroke="#fff" stroke-width="1.5"/><rect x="4" y="11" width="10" height="6" fill="none" stroke="#fff" stroke-width="1.5"/></svg><span>02 6700 1233</span></div>
  </div>

  <h4 style="left:602px">GLEN INNES OFFICE</h4>
  <div class="office" style="left:602px;width:240px">
    <div class="row"><svg width="16" height="22" viewBox="0 0 16 22"><path d="M8 1a7 7 0 0 0-7 7c0 5 7 13 7 13s7-8 7-13a7 7 0 0 0-7-7z" fill="none" stroke="#fff" stroke-width="1.6"/><circle cx="8" cy="8" r="2.5" fill="none" stroke="#fff" stroke-width="1.6"/></svg><span>218 Oak Street<br>Glen Innes</span></div>
    <div class="row"><svg width="18" height="18" viewBox="0 0 24 24"><path fill="none" stroke="#fff" stroke-width="1.8" d="M6.6 10.8a15 15 0 0 0 6.6 6.6l2.2-2.2c.3-.3.7-.4 1-.2 1.1.4 2.3.6 3.6.6.6 0 1 .4 1 1V20c0 .6-.4 1-1 1A17 17 0 0 1 3 4c0-.6.4-1 1-1h3.5c.6 0 1 .4 1 1 0 1.3.2 2.5.6 3.6.1.3 0 .7-.2 1z"/></svg><span>02 6700 3311</span></div>
    <div class="row"><svg width="18" height="18" viewBox="0 0 18 18"><rect x="4" y="1" width="10" height="5" fill="none" stroke="#fff" stroke-width="1.5"/><rect x="1" y="6" width="16" height="7" fill="none" stroke="#fff" stroke-width="1.5"/><rect x="4" y="11" width="10" height="6" fill="none" stroke="#fff" stroke-width="1.5"/></svg><span>02 6700 3344</span></div>
  </div>

  <h4 style="left:874px">GUYRA OFFICE</h4>
  <div class="office" style="left:874px;width:240px">
    <div class="row"><svg width="16" height="22" viewBox="0 0 16 22"><path d="M8 1a7 7 0 0 0-7 7c0 5 7 13 7 13s7-8 7-13a7 7 0 0 0-7-7z" fill="none" stroke="#fff" stroke-width="1.6"/><circle cx="8" cy="8" r="2.5" fill="none" stroke="#fff" stroke-width="1.6"/></svg><span>75 Ridge Street<br>Guyra (by Appointment)</span></div>
    <div class="row"><svg width="18" height="18" viewBox="0 0 24 24"><path fill="none" stroke="#fff" stroke-width="1.8" d="M6.6 10.8a15 15 0 0 0 6.6 6.6l2.2-2.2c.3-.3.7-.4 1-.2 1.1.4 2.3.6 3.6.6.6 0 1 .4 1 1V20c0 .6-.4 1-1 1A17 17 0 0 1 3 4c0-.6.4-1 1-1h3.5c.6 0 1 .4 1 1 0 1.3.2 2.5.6 3.6.1.3 0 .7-.2 1z"/></svg><span>02 6700 1200</span></div>
    <div class="row"><svg width="18" height="18" viewBox="0 0 18 18"><rect x="4" y="1" width="10" height="5" fill="none" stroke="#fff" stroke-width="1.5"/><rect x="1" y="6" width="16" height="7" fill="none" stroke="#fff" stroke-width="1.5"/><rect x="4" y="11" width="10" height="6" fill="none" stroke="#fff" stroke-width="1.5"/></svg><span>02 6700 1233</span></div>
  </div>

  <div class="abs" style="left:0;top:255px;width:1200px;height:1px;background:rgba(255,255,255,.15)"></div>
  <div class="abs" style="left:0;top:270px;width:1200px;text-align:center;font-size:14px;color:#d5dce6">©<b style="color:#fff">RTM Law</b>- 2017. All Rights Reserved.</div>
</footer>

</body>
</html>
```